Card for Maori themed strategy game

Visual design of a type of card from a board game.
The card has a front and a back, back being a single large image, and with one of three small icons (in white) to represent which of the three periods of the game it is from, but otherwise there is no difference in the backs.
The front side carries most of the information, and hopefully an attractive design. Functionally, from top to bottom it has a title, a large text field, a type line, another text field, and some tracking information at the very bottom. Current layout with placeholder art is attached.
Note that the relative size of the two text boxes will vary from card to card.
The colour pallete is intended to be red black and white, for this particular design focusing primarily on red.

```html
<!DOCTYPE html>
<html lang="en">
<head>
<meta charset="utf-8">
<title>Maori Strategy Game – Card Designs</title>
<link rel="stylesheet" href="https://fonts.googleapis.com/css2?family=Oswald:wght@500;600&family=Open+Sans:ital,wght@0,400;0,600;0,700;1,400&display=swap">
<style>
  :root{
    --backdrop:#ececec;
    --card-red:#8f2419;
    --card-red-deep:#7a1c13;
    --frame-line:#b8473a;
    --panel-orange:#c9533d;
    --panel-border:#f2d9cf;
    --ink-dark:#2e110c;
    --ink-light:#ffffff;
    --mask-dark:#3a140e;
    --mask-mid:#7c2a1c;
  }
  *{box-sizing:border-box;margin:0;padding:0}
  html,body{width:1200px;height:1000px;overflow:hidden}
  body{background:var(--backdrop);position:relative;font-family:"Open Sans",Arial,sans-serif;color:var(--ink-light)}

  .card{position:absolute;width:200px;height:276px;background:var(--card-red);border-radius:3px;overflow:hidden}
  .card::before{content:"";position:absolute;inset:6px;border:1px solid var(--frame-line);pointer-events:none}
  .card::after{content:"";position:absolute;inset:10px;border:1px solid var(--card-red-deep);pointer-events:none}

  /* card backs */
  .back-art{position:absolute;left:28px;top:18px;width:144px;height:222px;border-radius:50% 50% 46% 46%;
    background:radial-gradient(ellipse at 50% 45%,var(--mask-mid) 0%,var(--mask-dark) 75%)}
  .period-badge{position:absolute;left:78px;bottom:7px;width:44px;height:26px;background:var(--ink-dark);
    border-radius:22px 22px 0 0;display:flex;align-items:center;justify-content:center;padding-top:4px}
  .period-icon{width:18px;height:12px;background:var(--ink-light);border-radius:2px;opacity:.9}

  /* card fronts */
  .front{display:flex;flex-direction:column;align-items:center;padding:17px 16px 22px}
  .title{width:168px;height:26px;background:var(--ink-dark);border:1.5px solid var(--panel-border);
    border-radius:50% 50% 0 0 / 6px 6px 0 0;
    font-family:"Oswald",Arial,sans-serif;font-weight:600;font-size:13px;text-transform:uppercase;
    display:flex;align-items:center;justify-content:center;letter-spacing:.2px;position:relative;z-index:1}
  .rules{margin-top:6px;width:148px;background:var(--panel-orange);border:2px solid var(--panel-border);
    padding:3px 5px;text-align:center;font-weight:600;font-size:9.5px;line-height:1.2;z-index:1}
  .rules.small{font-size:6.8px;font-weight:600;line-height:1.25}
  .rules.list{font-size:8.4px}
  .rules.large{font-size:9.8px}
  .card-type{margin-top:8px;min-width:72px;padding:2px 8px;background:var(--ink-dark);border:1px solid var(--panel-border);
    font-weight:700;font-size:9.5px;text-align:center;z-index:1}
  .timing{margin-top:3px;font-style:italic;font-size:7.4px;z-index:1}
  .lore{margin-top:6px;width:150px;flex:1;background:var(--panel-orange);padding:8px 6px;
    font-size:6.1px;line-height:1.35;text-align:center;z-index:1}
  .lore.tall{margin-top:12px}
</style>
</head>
<body>

  <!-- backs -->
  <div class="card back" style="left:272px;top:62px">
    <div class="back-art" role="img" aria-label="Carved mask artwork in dark brown and red"></div>
    <div class="period-badge"><span class="period-icon" role="img" aria-label="Canoe icon: first period"></span></div>
  </div>
  <div class="card back" style="left:509px;top:62px">
    <div class="back-art" role="img" aria-label="Carved mask artwork in dark brown and red"></div>
    <div class="period-badge"><span class="period-icon" role="img" aria-label="Crossed weapons icon: second period"></span></div>
  </div>
  <div class="card back" style="left:730px;top:62px">
    <div class="back-art" role="img" aria-label="Carved mask artwork in dark brown and red"></div>
    <div class="period-badge"><span class="period-icon" role="img" aria-label="Sailing ship icon: third period"></span></div>
  </div>

  <!-- fronts, row one -->
  <div class="card front" style="left:270px;top:362px">
    <h2 class="title">Claiming the Land</h2>
    <p class="rules">Place a Marae in the newly settled territory.</p>
    <p class="card-type">Reaction</p>
    <p class="timing">Play when you settle a new territory</p>
    <p class="lore">Maori placed great value on their own whakapapa (heritage), and also wished to know the whakapapa of this new land. The arrivals made legends explaining how their gods and ancestors had shaped Aotearoa. This whakapapa helped them to understand their land, as well as giving them an ancestral claim to the territory. The people of Rakiwhenua say their ancestor Haumoa went inland one day to repair his waka, but the day was long and the work hard, so he urinated frequently, carving out the great Waihaumoa river.</p>
  </div>

  <div class="card front" style="left:508px;top:362px">
    <h2 class="title">Terrace Gardens</h2>
    <p class="rules">Gain six food from your harvest of kumara</p>
    <p class="card-type">Action</p>
    <p class="lore tall">With the moa extinct and the population growing, Maori turned to farming. Their key crop was kumara, a tropical plant which needed complex techniques to grow in the much colder Aotearoa. Gardens were dug into north facing hills (the warmest side), and laid with stones to further trap heat. The soil was mixed with gravel to make it drain well and had to be watched for birds and caterpillars that could damage the crop. Many of these gardens can be seen today, in the shape of reformed hills.</p>
  </div>

  <div class="card front" style="left:730px;top:362px">
    <h2 class="title">Influenza Epidemic</h2>
    <p class="rules small">Each other player is afflicted by the Influenza in Patu order. If they have five or more Rangatira, they downgrade two Rangatira to Ware. Otherwise, they downgrade one Rangatira to Ware</p>
    <p class="card-type">Tribal</p>
    <p class="lore tall">Of all the new diseases Maori caught from their visitors, by far the most common. Infected patients cough constantly, the virus riding tiny particles of spit to a new host. Flu was not an especially lethal disease, but was the fastest to spread. Influenza is also notable for mutating quickly. A population would a year or two another strain would develop and cause its own epidemic.</p>
  </div>

  <!-- fronts, row two -->
  <div class="card front" style="left:270px;top:656px">
    <h2 class="title">The Tairanga Lands</h2>
    <p class="rules">Place a two neutral ware in a unoccupied coastal territory.</p>
    <p class="card-type">Tribal</p>
    <p class="lore tall">Tairanga was a noble child died young, and upon his grave was planted a sapling. This tree grew great and strong, eventually being carved into the mighty waka Tairanga. The great canoe set out for Aotearoa, captained by Te Roanuku. The waka made landfall near Whangaroto before being carried by hand across Taumata. It then sailed up and down the west coast, leaving hapu scattered across the central north island, a people to this day called the Tairanga confederation.</p>
  </div>

  <div class="card front" style="left:508px;top:656px">
    <h2 class="title">Fortification</h2>
    <p class="rules list">Choose one of...<br>- Place a Pa in each of two nutral territories<br>- Upgrade one nuetral Pa to a Great Pa</p>
    <p class="card-type">Tribal</p>
    <p class="lore">Unlike Kainga and Marae which were built near resources, Pa were erected on defensible land like hills, peninsulas, lakes and gorges, where the hapu could shelter in times of conflict. A Pa was ringed with a palisade wall made of wooden stakes planted deep in the earth, and often with a deep ditch dug outside to further slow attackers. This wall protected an interior with housing, fighting platforms, and deep pits dug to store kumara for a siege.</p>
  </div>

  <div class="card front" style="left:730px;top:656px">
    <h2 class="title">Heavy Artillery</h2>
    <p class="rules large">Spend a trade good to borrow the cannon. Ignore any enemy Pa during this combat</p>
    <p class="card-type">Reaction</p>
    <p class="timing">Play before rolling when you attack</p>
    <p class="lore">Muskets in the became a common weapon, but the Europeans had much greater firepower at their disposal. Light cannons were used by some sailors for defense against pirates or for whaling, and unscrupulous traders would loan them if the price was right. The wooden, high walled Pa of the Contact period could not hope to stand against cannon, as many found to their cost.</p>
  </div>

</body>
</html>
```